Unique Beautiful Realtor business card

I need a unique business card that includes my logo, my firms logo, my picture and phone number. The colors should compliment my logo.

Target Market(s)

People who want to buy or sell a home in South Florida

Contact Information for Business Card

Use two sides and work with the DRM Coastal Homes logo as a theme.
The Harlow Benton should be small and discreet, it is a requirement to be there but should be small. My photo should be integrated artistically.

Font styles to use
Serif
Sans Serif

Colors

Designer to choose colors to be used in the design.

Requirements
Must have
• My logo, Harlow Benton logo, my photo, my phone number, (954-283-6091) and my website address. (www.drmcoastalhomes.example)
• Also my name, Dana R. Moreland, PA, Realtor
• Also “The Pet Friendly Realtor”

```html
<!DOCTYPE html>
<html lang="en">
<head>
<meta charset="utf-8">
<title>DRM Coastal Homes – Business Card</title>
<link href="https://fonts.googleapis.com/css2?family=Montserrat:wght@500;600&family=Lato:wght@400;700&display=swap" rel="stylesheet">
<style>
  :root {
    --stage: #3a3431;
    --card: #0c0c0c;
    --card-edge: #1c1c1c;
    --accent-yellow: #f2d21b;
    --accent-lime: #c9c52a;
    --logo-blue: #1f5fae;
    --silver: #d9d9d9;
    --text-grey: #bdbdbd;
    --text-white: #f2f2f2;
    --firm-red: #c8102e;
    --photo-dark: #2c2f36;
    --photo-light: #6d6a70;
  }
  * { box-sizing: border-box; margin: 0; padding: 0; }
  html, body { width: 1200px; height: 844px; overflow: hidden; }
  body {
    background: var(--stage);
    font-family: "Lato", Arial, sans-serif;
    position: relative;
  }
  .card {
    position: absolute;
    top: 272px;
    width: 525px;
    height: 300px;
    background: var(--card);
    border: 1px solid var(--card-edge);
    box-shadow: 0 8px 24px rgba(0,0,0,.45);
    overflow: hidden;
  }
  .card--front { left: 50px; }
  .card--back { left: 625px; }

  /* Front */
  .agent-photo {
    position: absolute;
    left: 40px;
    bottom: 0;
    width: 240px;
    height: 205px;
    background: linear-gradient(180deg, var(--photo-light) 0%, var(--photo-dark) 100%);
    border-radius: 90px 90px 0 0;
  }
  .brand {
    position: absolute;
    display: flex;
    align-items: center;
    gap: 8px;
    font-family: "Montserrat", Arial, sans-serif;
    font-weight: 600;
    letter-spacing: 1.5px;
    text-transform: uppercase;
  }
  .brand__mark { width: 12px; height: 12px; }
  .card--front .brand {
    top: 40px;
    left: 250px;
    font-size: 20px;
    color: var(--logo-blue);
  }
  .card--front .brand__mark { background: var(--accent-yellow); }
  .contact {
    position: absolute;
    left: 262px;
    top: 96px;
  }
  .contact__name {
    font-family: "Montserrat", Arial, sans-serif;
    font-weight: 500;
    font-size: 19px;
    letter-spacing: 1.5px;
    color: var(--accent-lime);
    text-transform: uppercase;
  }
  .contact__title {
    font-size: 13px;
    color: var(--text-grey);
    margin-top: 2px;
  }
  .contact__line {
    display: flex;
    align-items: center;
    gap: 7px;
    font-size: 13.5px;
    color: var(--text-white);
    margin-top: 6px;
  }
  .contact__icon { width: 13px; height: 13px; flex: none; }
  .tagline {
    position: absolute;
    left: 262px;
    top: 218px;
    font-family: "Montserrat", Arial, sans-serif;
    font-weight: 500;
    font-size: 15px;
    color: var(--accent-yellow);
    text-transform: uppercase;
    letter-spacing: .5px;
  }

  /* Back */
  .card--back .brand {
    top: 110px;
    left: 0;
    width: 100%;
    justify-content: center;
    font-size: 24px;
    color: var(--silver);
  }
  .card--back .brand__mark { border: 2px solid var(--silver); }
  .firm {
    position: absolute;
    top: 178px;
    left: 0;
    width: 100%;
    text-align: center;
    line-height: 1.15;
  }
  .firm__name {
    font-family: "Montserrat", Arial, sans-serif;
    font-weight: 600;
    font-size: 12px;
    color: var(--firm-red);
    letter-spacing: 1px;
    text-transform: uppercase;
  }
  .firm__office {
    font-size: 9px;
    color: var(--text-grey);
    letter-spacing: 1px;
    text-transform: uppercase;
  }
</style>
</head>
<body>
  <section class="card card--front" aria-label="Business card front">
    <div class="agent-photo" role="img" aria-label="Portrait photo of the realtor in a grey blazer"></div>
    <div class="brand"><span class="brand__mark"></span>DRM Coastal Homes</div>
    <div class="contact">
      <p class="contact__name">Dana R. Moreland</p>
      <p class="contact__title">PA, Realtor</p>
      <p class="contact__line">
        <svg class="contact__icon" viewBox="0 0 16 16" aria-hidden="true"><circle cx="8" cy="8" r="8" fill="#f2d21b"/><path d="M5 4.5l1.6-.4.9 2-1 .8a5 5 0 0 0 2.6 2.6l.8-1 2 .9-.4 1.6C8.5 11.5 4.5 7.5 5 4.5z" fill="#0c0c0c"/></svg>
        954-283-6091
      </p>
      <p class="contact__line">
        <svg class="contact__icon" viewBox="0 0 16 16" aria-hidden="true"><circle cx="8" cy="8" r="8" fill="#c9c52a"/><circle cx="8" cy="8" r="4.5" fill="none" stroke="#0c0c0c" stroke-width="1.2"/><path d="M3.5 8h9M8 3.5c-2 2.5-2 6.5 0 9M8 3.5c2 2.5 2 6.5 0 9" fill="none" stroke="#0c0c0c" stroke-width="1"/></svg>
        www.drmcoastalhomes.example
      </p>
    </div>
    <p class="tagline">The Pet Friendly Realtor</p>
  </section>

  <section class="card card--back" aria-label="Business card back">
    <div class="brand"><span class="brand__mark"></span>DRM Coastal Homes</div>
    <div class="firm">
      <p class="firm__name">Harlow Benton</p>
      <p class="firm__office">Bayview Office</p>
    </div>
  </section>
</body>
</html>
```